Landing page для Детский клуб "Тиливки"
Название сайта (домена, или проекта)
Детский клуб "Тиливки"
Цель: Создать современный одностраничный сайт (лендинг) с возможностью в будущем добавлять внутренние страницы. Основная задача — презентовать клуб, его методику и преподавателей, сформировать образ надежного и профессионального детского центра. Итоговая цель — убедить родителей детей 1-7 лет записать ребенка на пробное занятие.
Целевая аудитория: Родители (преимущественно мамы) детей 1-7 лет в Ижевске, для которых важны качество, безопасность, индивидуальный подход, санитарная обработка материалов и профессионализм педагогов.
Детальное ТЗ, логотип, фотографии (для использования на лэндинге) можно найти по ссылке – https://files.nebolka-cloud.ru/d/kqmrtZa-WPn4LH
Адаптивность сайта
Десктопная версия, Версия для планшетов, Версия для телефонов

```html
<!DOCTYPE html>
<html lang="ru">
<head>
<meta charset="utf-8">
<title>Детский клуб "Тиливки"</title>
<link rel="stylesheet" href="https://fonts.googleapis.com/css2?family=Nunito:wght@400;600;800&display=swap">
<style>
  :root{
    --ink:#3b1a5e;
    --text:#2b2b33;
    --pink:#d6468f;
    --pink-soft:#e0559b;
    --cream:#f8f2ee;
    --lavender:#efecfa;
    --white:#ffffff;
  }
  *{margin:0;padding:0;box-sizing:border-box}
  html,body{width:1200px;height:915px;overflow:hidden;background:var(--white)}
  body{font-family:"Nunito",sans-serif;color:var(--text);position:relative}

  .hero-title{position:absolute;left:91px;top:-34px;font-size:50px;font-weight:800;color:var(--ink);line-height:1.1}
  .hero-lead{position:absolute;left:91px;top:36px;font-size:16px;line-height:27px;color:var(--text)}
  .btn-primary{position:absolute;left:91px;top:122px;width:307px;height:51px;border-radius:26px;background:var(--pink);color:var(--white);font-size:15px;font-weight:600;display:flex;align-items:center;justify-content:center;text-decoration:none}
  .contact-card{position:absolute;left:91px;top:226px;width:281px;height:112px;border-radius:28px;background:var(--cream);padding:24px 0 0 26px}
  .contact-item{display:flex;align-items:center;gap:10px;font-size:13px;height:20px;margin-bottom:22px}
  .contact-item svg{width:18px;height:18px;flex:none}
  .hero-photo{position:absolute;left:523px;top:0;width:586px;height:393px;border-radius:0 0 48px 48px;background:linear-gradient(135deg,#f7efa0 0%,#fbf6d8 45%,#f4dfe6 75%,#c9e3f4 100%)}

  .why{position:absolute;left:0;top:471px;width:1200px;height:470px;background:var(--lavender);border-radius:70px 70px 0 0}
  .why-title{position:absolute;left:91px;top:46px;font-size:32px;font-weight:800;color:var(--ink);display:flex;align-items:center;gap:16px}
  .why-title svg{width:28px;height:26px}
  .why-photo{position:absolute;left:91px;top:211px;width:845px;height:260px;border-radius:34px 34px 0 0;background:linear-gradient(180deg,#e9e4dc 0%,#f1ece6 45%,#e4dcd4 100%)}
  .feature{position:absolute;top:117px;width:239px;height:118px;border-radius:26px;background:var(--white);padding:26px 0 0 26px}
  .feature svg{width:20px;height:20px;display:block;margin-bottom:18px}
  .feature p{font-size:13px;line-height:18px;color:var(--text)}
  .feature--exp{left:351px}
  .feature--system{left:610px}
  .feature--games{left:871px}
  .feature--games svg{margin-bottom:10px}
</style>
</head>
<body>
  <header class="hero">
    <h1 class="hero-title">в его таланты.</h1>
    <p class="hero-lead">Индивидуальные и групповые занятия<br>для детей 1-7 лет в Ижевске.</p>
    <a class="btn-primary" href="#">Записаться на первое занятие</a>
    <div class="contact-card">
      <div class="contact-item">
        <svg viewBox="0 0 24 24" fill="none" stroke="#d6468f" stroke-width="2"><path d="M12 21s-7-6.2-7-11.5A7 7 0 0 1 19 9.5C19 14.8 12 21 12 21z"/><circle cx="12" cy="9.5" r="2.5"/></svg>
        улица Садовая, 14, Ижевск
      </div>
      <div class="contact-item">
        <svg viewBox="0 0 24 24" fill="none" stroke="#d6468f" stroke-width="2"><path d="M5 4h4l2 5-2.5 1.5a11 11 0 0 0 5 5L15 13l5 2v4a2 2 0 0 1-2 2A16 16 0 0 1 3 6a2 2 0 0 1 2-2z"/></svg>
        +7 (900) 123-45-67
      </div>
    </div>
    <div class="hero-photo" role="img" aria-label="Фото: педагог и ребёнок играют с разноцветными кубиками-подарками за столом"></div>
  </header>

  <section class="why">
    <h2 class="why-title">Почему Тиливки?
      <svg viewBox="0 0 24 22"><path fill="#d6468f" d="M12 21.5 2.6 12.4A5.8 5.8 0 0 1 12 4.3a5.8 5.8 0 0 1 9.4 8.1z"/></svg>
    </h2>
    <div class="why-photo" role="img" aria-label="Фото: группа детей занимается с развивающими играми за длинным столом"></div>
    <div class="feature feature--exp">
      <svg viewBox="0 0 24 24" fill="none" stroke="#d6468f" stroke-width="2"><circle cx="12" cy="9" r="5"/><path d="M8.5 13 7 21l5-3 5 3-1.5-8"/></svg>
      <p>15 лет опыта</p>
    </div>
    <div class="feature feature--system">
      <svg viewBox="0 0 24 24" fill="none" stroke="#d6468f" stroke-width="2"><path d="M12 3 4 6v6c0 5 3.5 8 8 9 4.5-1 8-4 8-9V6z"/><path d="m9 12 2 2 4-4"/></svg>
      <p>Авторская система</p>
    </div>
    <div class="feature feature--games">
      <svg viewBox="0 0 24 24" fill="none" stroke="#d6468f" stroke-width="2"><path d="M3 5h6a3 3 0 0 1 3 3v12a2 2 0 0 0-2-2H3zM21 5h-6a3 3 0 0 0-3 3v12a2 2 0 0 1 2-2h7z"/></svg>
      <p>Крупнейшая база<br>развивающих игр</p>
    </div>
  </section>
</body>
</html>
```